Harborline Facility Systems needs a business card design with logo

need a business card and log design for a company called "Harborline Facility Systems". we improve building energy efficiency and save energy costs through building automation systems for commercial buildings such as hospitals, office buildings, universities, etc. The final design should communicate elements such as "precision", "energy efficiency", "green buildings". back side should list our service offerings

```html
<!DOCTYPE html>
<html lang="en">
<head>
<meta charset="utf-8">
<title>Harborline Facility Systems – Business Card</title>
<link href="https://fonts.googleapis.com/css2?family=Oswald:wght@400;500&family=Open+Sans:wght@400;600&display=swap" rel="stylesheet">
<style>
  :root {
    --navy: #0f2b60;
    --green: #4e9424;
    --white: #ffffff;
    --backdrop: #d6d6d6;
    --rule: #e4e4e4;
    --ink: #0f2b60;
  }
  * { margin: 0; padding: 0; box-sizing: border-box; }
  html, body { width: 1200px; height: 802px; overflow: hidden; }
  body { background: var(--backdrop); position: relative; font-family: "Open Sans", sans-serif; }

  .card { position: absolute; top: 274px; width: 442px; height: 264px; background: var(--white); overflow: hidden; }
  .card--front { left: 136px; }
  .card--back { left: 624px; }

  /* Front */
  .brand-strip { position: absolute; left: 0; top: 0; width: 133px; height: 100%;
    display: flex; flex-direction: column; align-items: center; justify-content: center; gap: 12px; }
  .brand-strip__dot { width: 34px; height: 34px; border-radius: 50%; background: var(--green); }
  .brand-strip__name { font-family: "Oswald", sans-serif; font-weight: 500; font-size: 15px; line-height: 1.15;
    color: var(--navy); text-align: center; text-transform: uppercase; letter-spacing: 0.5px; }
  .info-panel { position: absolute; left: 133px; top: 0; width: 309px; height: 100%; background: var(--navy);
    color: var(--white); text-align: right; padding-right: 20px; }
  .person__name { position: absolute; right: 20px; top: 33px; font-family: "Oswald", sans-serif; font-weight: 400;
    font-size: 19px; letter-spacing: -0.2px; line-height: 1; }
  .person__title { position: absolute; right: 20px; top: 55px; font-size: 12px; line-height: 1; }
  .contact { position: absolute; right: 20px; top: 128px; list-style: none; font-size: 12px; line-height: 16px; }
  .contact li { display: flex; justify-content: flex-end; align-items: center; gap: 3px; }
  .contact svg { width: 10px; height: 10px; fill: var(--white); }
  .address { position: absolute; right: 20px; top: 199px; font-size: 12px; line-height: 16px; font-style: normal; }

  /* Back */
  .mark-dot { position: absolute; left: 50%; top: 44px; width: 58px; height: 58px; margin-left: -29px;
    border-radius: 50%; background: var(--green); }
  .company-name { position: absolute; left: 0; right: 0; top: 138px; text-align: center;
    font-family: "Oswald", sans-serif; font-weight: 500; font-size: 24px; line-height: 1; color: var(--navy);
    text-transform: uppercase; letter-spacing: -0.2px; }
  .divider { position: absolute; left: 64px; width: 315px; top: 196px; height: 1px; background: var(--rule); border: 0; }
  .services { position: absolute; left: 64px; top: 208px; width: 320px; list-style: none;
    display: grid; grid-template-columns: 110px 108px 110px; grid-auto-flow: column; grid-template-rows: 16px 16px;
    font-size: 12.5px; line-height: 16px; color: var(--ink); }
  .services li { white-space: nowrap; }
  .services li::before { content: ""; display: inline-block; width: 5px; height: 5px; border-radius: 50%;
    background: var(--green); margin-right: 4px; vertical-align: middle; position: relative; top: -1px; }
  .services li:nth-child(n+3)::before { margin-right: 10px; margin-left: 2px; }
</style>
</head>
<body>
  <section class="card card--front">
    <div class="brand-strip">
      <span class="brand-strip__dot"></span>
      <span class="brand-strip__name">Harborline<br>Facility<br>Systems</span>
    </div>
    <div class="info-panel">
      <h1 class="person__name">DANA WHITFIELD</h1>
      <p class="person__title">Managing Director</p>
      <ul class="contact">
        <li>044-123 456 789
          <svg viewBox="0 0 10 10"><path d="M1 3.5C1 2 2.5 1.5 5 1.5S9 2 9 3.5V4.5H7V3.5H3V4.5H1Z M2.5 5H7.5L8.5 8.5H1.5Z"/></svg></li>
        <li>044-123 456 789
          <svg viewBox="0 0 10 10"><path d="M3 0.5H7A0.8 0.8 0 0 1 7.8 1.3V8.7A0.8 0.8 0 0 1 7 9.5H3A0.8 0.8 0 0 1 2.2 8.7V1.3A0.8 0.8 0 0 1 3 0.5ZM3 1.5V7.5H7V1.5Z"/></svg></li>
        <li>info@webname.com
          <svg viewBox="0 0 10 10"><path d="M0.5 2H9.5V8H0.5ZM1.5 3V3.3L5 5.6L8.5 3.3V3Z"/></svg></li>
        <li>www.websitename.com
          <svg viewBox="0 0 10 10"><circle cx="5" cy="5" r="4.5"/><path d="M3 3.5L5 2.5L6.5 4L5 5.5L6 7.5L4 7L3.5 5Z" fill="#0f2b60"/></svg></li>
      </ul>
      <address class="address">12345, Address Goes Here<br>Country Name, 123456</address>
    </div>
  </section>

  <section class="card card--back">
    <span class="mark-dot"></span>
    <h2 class="company-name">Harborline Facility Systems</h2>
    <hr class="divider">
    <ul class="services">
      <li>Service point1</li>
      <li>Service point2</li>
      <li>Service point3</li>
      <li>Service point4</li>
      <li>Service point5</li>
      <li>Service point6</li>
    </ul>
  </section>
</body>
</html>
```